Letterhead Design Project

Attached is our new Logo and a copy of our old letter head
Looking to rebrand with our new logo

Reason: I want to show a business card design

Industry/Entity Type

Film Production

Colors

Requirements
Must have
• The information on the old letterhead

```html
<!DOCTYPE html>
<html lang="en">
<head>
<meta charset="utf-8">
<title>Vantre International – Letterhead &amp; Business Card</title>
<link href="https://fonts.googleapis.com/css2?family=Ubuntu:wght@400;500;700&display=swap" rel="stylesheet">
<style>
  :root {
    --page-bg: #d6d6d8;
    --paper: #ffffff;
    --ink: #4a4a4a;
    --ink-dark: #1d1d1d;
    --ink-soft: #6b6b6b;
    --brand-blue: #1e8fc8;
    --brand-orange: #ee7f2d;
    --tint-orange: #f8dcc4;
    --tint-blue: #cfe2f2;
  }
  * { box-sizing: border-box; margin: 0; padding: 0; }
  html, body { width: 1200px; height: 1000px; overflow: hidden; }
  body {
    background: var(--page-bg);
    font-family: "Ubuntu", Arial, sans-serif;
    color: var(--ink);
    position: relative;
  }

  /* Letterhead */
  .letterhead {
    position: absolute; left: 300px; top: 78px;
    width: 597px; height: 842px;
    background: var(--paper);
  }
  .letterhead__contact {
    position: absolute; left: 66px; top: 43px;
    font-size: 10.5px; line-height: 15px; color: var(--ink);
  }
  .contact-row { display: flex; align-items: center; gap: 8px; }
  .contact-row svg { width: 12px; height: 12px; }
  .letterhead__rule {
    position: absolute; left: 52px; top: 107px; width: 360px; height: 1.5px;
    background: linear-gradient(90deg, var(--brand-orange), rgba(238,127,45,0));
  }
  .letterhead__tagline {
    position: absolute; left: 66px; top: 114px;
    font-size: 9.5px; font-weight: 700; color: var(--ink-soft); letter-spacing: .2px;
  }
  .brand {
    display: flex; align-items: center; gap: 8px;
    color: var(--brand-blue); font-weight: 700; text-transform: uppercase;
    line-height: 1;
  }
  .brand__mark { width: 14px; height: 14px; border-radius: 50%; background: var(--brand-blue); flex: none; }
  .brand__name { display: flex; flex-direction: column; }
  .letterhead .brand { position: absolute; right: 56px; top: 38px; }
  .letterhead .brand__name { font-size: 30px; letter-spacing: 1px; }
  .letterhead .brand__name small { font-size: 13.5px; letter-spacing: 2.6px; margin-top: 6px; }

  .letterhead__footer-rule {
    position: absolute; left: 52px; top: 751px; width: 498px; height: 1.5px;
    background: linear-gradient(90deg, var(--brand-blue), rgba(30,143,200,0));
  }
  .divisions {
    position: absolute; display: flex; align-items: stretch;
  }
  .letterhead .divisions { left: 66px; top: 765px; }
  .divisions__owner { font-size: 9px; line-height: 13px; color: var(--ink); padding-right: 6px; margin-top: 11px; }
  .divisions__owner strong { color: var(--ink-dark); font-weight: 700; }
  .divisions__owner .owner-name { color: var(--brand-blue); font-weight: 700; }
  .divisions__list {
    border-left: 1px solid var(--ink);
    padding-left: 8px; list-style: none;
    font-size: 9px; line-height: 14.5px; font-weight: 500; color: var(--ink);
    text-transform: uppercase;
  }
  .divisions__list .div-name { color: var(--brand-blue); font-weight: 700; }

  /* Business cards */
  .card {
    position: absolute; width: 276px; height: 158px; overflow: hidden;
    box-shadow: 0 2px 8px rgba(0,0,0,.18);
  }
  .card--front {
    left: 912px; top: 318px;
    background: linear-gradient(30deg, var(--tint-orange) 0%, #fff 55%, #eef5fb 100%);
  }
  .card--back {
    left: 912px; top: 520px;
    background: linear-gradient(300deg, var(--tint-orange) 0%, #fff 45%, var(--tint-blue) 100%);
  }
  .card--front .brand { position: absolute; left: 34px; top: 22px; }
  .card--front .brand__name { font-size: 24px; letter-spacing: 1px; }
  .card--front .brand__name small { font-size: 10.5px; letter-spacing: 2px; margin-top: 5px; }
  .card__rule-blue {
    position: absolute; left: 150px; top: 28px; width: 126px; height: 1.5px;
    background: linear-gradient(90deg, rgba(30,143,200,0), var(--brand-blue));
  }
  .card__contact {
    position: absolute; left: 168px; top: 78px; font-size: 8.5px; line-height: 13px; color: var(--ink);
  }
  .card__contact .contact-row svg { width: 10px; height: 10px; }
  .card__rule-orange {
    position: absolute; left: 0; top: 110px; width: 170px; height: 1.5px;
    background: linear-gradient(90deg, var(--brand-orange), rgba(238,127,45,0));
  }
  .card__address {
    position: absolute; left: 20px; top: 118px; font-size: 8.5px; line-height: 13px; color: var(--ink);
  }
  .card--back .divisions { left: 20px; top: 86px; }
  .card--back .divisions__owner { font-size: 7.5px; line-height: 11px; margin-top: 8px; }
  .card--back .divisions__list { font-size: 7.5px; line-height: 12px; padding-left: 6px; }
</style>
</head>
<body>

<section class="letterhead" aria-label="Vantre International letterhead">
  <div class="letterhead__contact">
    <p>P.O. Box 482 Millbrook QLD 4390</p>
    <p>P.O.Box 317 Harwood NSW 2185</p>
    <p class="contact-row">
      <svg viewBox="0 0 12 12" aria-hidden="true"><circle cx="6" cy="6" r="5.3" fill="none" stroke="#4a4a4a" stroke-width="1"/><path d="M4 3.2l1.2 1.4-.6.8c.4.9 1 1.5 1.9 1.9l.8-.6 1.4 1.2-.7 1c-2.4-.3-4.4-2.3-4.7-4.7z" fill="#4a4a4a"/></svg>
      0400 512 786
    </p>
    <p class="contact-row">
      <svg viewBox="0 0 12 12" aria-hidden="true"><rect x="0.8" y="2.5" width="10.4" height="7" fill="none" stroke="#4a4a4a" stroke-width="1"/><path d="M0.8 2.5L6 6.6l5.2-4.1" fill="none" stroke="#4a4a4a" stroke-width="1"/></svg>
      hello@vantre.com.au
    </p>
  </div>
  <div class="letterhead__rule"></div>
  <p class="letterhead__tagline">SUPPLY &amp; MANAGEMENT OF INFRASTRUCTURE &amp; LOGISTICS</p>

  <div class="brand">
    <span class="brand__mark"></span>
    <span class="brand__name">Vantre<small>International</small></span>
  </div>

  <div class="letterhead__footer-rule"></div>
  <div class="divisions">
    <p class="divisions__owner">DIVISIONS OF<br><span class="owner-name">VANTRE INTERNATIONAL PTY LTD</span><br>ACN 204 618 379&nbsp; ABN 52 204 618 379</p>
    <ul class="divisions__list">
      <li><span class="div-name">Vantre</span> Film Services</li>
      <li><span class="div-name">Vantre</span> Pilot Esco</li>
      <li><span class="div-name">Vantre</span> Tour Management</li>
      <li><span class="div-name">Vantre</span> Driver</li>
    </ul>
  </div>
</section>

<section class="card card--front" aria-label="Business card front">
  <div class="card__rule-blue"></div>
  <div class="brand">
    <span class="brand__mark"></span>
    <span class="brand__name">Vantre<small>International</small></span>
  </div>
  <div class="card__contact">
    <p class="contact-row">
      <svg viewBox="0 0 12 12" aria-hidden="true"><circle cx="6" cy="6" r="5.3" fill="none" stroke="#4a4a4a" stroke-width="1"/><path d="M4 3.2l1.2 1.4-.6.8c.4.9 1 1.5 1.9 1.9l.8-.6 1.4 1.2-.7 1c-2.4-.3-4.4-2.3-4.7-4.7z" fill="#4a4a4a"/></svg>
      0400 512 786
    </p>
    <p class="contact-row">
      <svg viewBox="0 0 12 12" aria-hidden="true"><rect x="0.8" y="2.5" width="10.4" height="7" fill="none" stroke="#4a4a4a" stroke-width="1"/><path d="M0.8 2.5L6 6.6l5.2-4.1" fill="none" stroke="#4a4a4a" stroke-width="1"/></svg>
      hello@vantre.com.au
    </p>
  </div>
  <div class="card__rule-orange"></div>
  <div class="card__address">
    <p>P.O. Box 482 Millbrook QLD 4390</p>
    <p>P.O.Box 317 Harwood NSW 2185</p>
  </div>
</section>

<section class="card card--back" aria-label="Business card back">
  <div class="divisions">
    <p class="divisions__owner">DIVISIONS OF<br><span class="owner-name">VANTRE INTERNATIONAL PTY LTD</span><br>ACN 204 618 379&nbsp; ABN 52 204 618 379</p>
    <ul class="divisions__list">
      <li><span class="div-name">Vantre</span> Film Services</li>
      <li><span class="div-name">Vantre</span> Pilot Escorts</li>
      <li><span class="div-name">Vantre</span> Tour Management</li>
      <li><span class="div-name">Vantre</span> Driver</li>
    </ul>
  </div>
</section>

</body>
</html>
```